Postcard Design For House buying

I buy houses for cash that need a lot of repairs and need a post card that illustrate that, i would like one that is somehow cartoonish, I had an idea about a house and a man that was kicking to the house like you do with old cars and then he had some $ bills in his hand. This is just an idea and you should not limit yourself to that

Target Market(s)

Dallas TX (DFW)

Industry/Entity Type

Real Estate

Requirements
Must have
• A Text on the frot calling for action, like "Sell your house fast Call 512-740-3916"

```html
<!DOCTYPE html>
<html lang="en">
<head>
<meta charset="utf-8">
<title>Sell Your House Fast – Postcard</title>
<link rel="stylesheet" href="https://fonts.googleapis.com/css2?family=Arvo:wght@400;700&family=Lato:ital,wght@1,400;1,700&display=swap">
<style>
  :root {
    --orange: #f26a0f;
    --orange-text: #f5690c;
    --charcoal: #424242;
    --charcoal-dark: #353535;
    --white: #ffffff;
    --paper-grey: #e9e9e9;
    --body-text: #454545;
    --stage: #ececec;
    --button-rim: #bdbdbd;
    --photo-placeholder: #b9bcc2;
  }
  * { margin: 0; padding: 0; box-sizing: border-box; }
  html, body {
    width: 1200px; height: 825px; overflow: hidden;
    background: var(--stage);
  }
  .postcard {
    position: absolute; left: 40px; top: 9px;
    width: 875px; height: 630px;
    transform: scale(1.28); transform-origin: 0 0;
    background: var(--white);
    overflow: hidden;
    font-family: "Lato", sans-serif;
  }
  .band { position: absolute; left: 0; width: 100%; }
  .band-header { top: 0; height: 142px; background: var(--orange); }
  .band-dark { top: 149px; height: 208px; background: linear-gradient(180deg, #4c4c4c, var(--charcoal-dark)); }
  .band-accent { top: 365px; height: 10px; background: var(--orange); }
  .band-paper { top: 375px; height: 182px; background: linear-gradient(180deg, var(--white) 40%, var(--paper-grey)); }
  .band-rule { top: 557px; height: 7px; background: var(--charcoal); }
  .band-footer { top: 564px; height: 66px; background: var(--orange); }

  .photo-frame { position: absolute; left: 0; top: 0; width: 875px; height: 360px; }

  .headline {
    position: absolute; left: 37px; top: 36px;
    font-family: "Arvo", serif; font-weight: 700;
    font-size: 32px; line-height: 35px; color: var(--white);
    white-space: nowrap;
  }
  .benefits {
    position: absolute; left: 50px; top: 180px;
    list-style: none; color: var(--white);
    font-style: italic; font-size: 26px; line-height: 32.5px;
    white-space: nowrap;
  }
  .benefits li { position: relative; padding-left: 26px; }
  .benefits li::before {
    content: ""; position: absolute; left: 0; top: 9px;
    width: 15px; height: 15px; border-radius: 50%; background: var(--orange);
  }
  .brand-name {
    position: absolute; left: 72px; top: 393px;
    font-family: "Arvo", serif; font-weight: 700;
    font-size: 46px; line-height: 54px; color: var(--orange-text);
    white-space: nowrap;
  }
  .call-to-action {
    position: absolute; left: 42px; top: 470px;
    width: 402px; height: 135px; border-radius: 28px;
    background: linear-gradient(180deg, #4a4a4a, var(--charcoal-dark));
    border: 4px solid var(--button-rim);
    padding: 20px 0 0 22px;
    white-space: nowrap;
  }
  .cta-main {
    display: block; font-family: "Arvo", serif; font-weight: 400;
    font-size: 46px; line-height: 52px; color: var(--orange-text);
  }
  .cta-phone {
    display: block; font-family: "Arvo", serif; font-weight: 400;
    font-size: 27px; line-height: 34px; color: var(--white);
  }
  .intro {
    position: absolute; right: 43px; top: 422px;
    text-align: right; font-style: italic; white-space: nowrap;
    font-size: 20px; line-height: 25px; color: var(--body-text);
  }
  .website {
    position: absolute; right: 40px; top: 579px;
    font-style: italic; font-weight: 700; font-size: 21px;
    letter-spacing: 3.5px; color: var(--white); white-space: nowrap;
  }
</style>
</head>
<body>
  <main class="postcard">
    <div class="band band-header"></div>
    <div class="band band-dark"></div>
    <div class="band band-accent"></div>
    <div class="band band-paper"></div>
    <div class="band band-rule"></div>
    <div class="band band-footer"></div>

    <svg class="photo-frame" viewBox="0 0 875 360">
      <polygon points="467,20 875,20 875,322 432,322" fill="#ffffff"/>
      <polygon points="471,33 875,33 875,311 445,311" fill="#f26a0f"/>
      <polygon points="475,37 875,37 875,307 450,307" fill="var(--photo-placeholder)"
               role="img" aria-label="Photo of a large two-storey suburban house at dusk with lawn and driveway"/>
    </svg>

    <h1 class="headline">We buy houses for cash<br>that need a lot of repairs</h1>

    <ul class="benefits">
      <li>Lorem ipsum dolor sit lorem</li>
      <li>Lorem ipsum dolor sit amet</li>
      <li>Lorem ipsum dolor sit amet</li>
      <li>Lorem ipsum dolor sit dol</li>
    </ul>

    <div class="brand-name">Your logo here</div>

    <div class="call-to-action">
      <span class="cta-main">Sell your house</span>
      <span class="cta-phone">fast Call 512-740-3916</span>
    </div>

    <p class="intro">Lorem ipsum dolor sit amet, consectetuer<br>adipiscing elit, sed diam nonummy nibh<br>smod tincidunt ut laoreet dolore magna<br>ghaliquam erat volutpat. Lorem ipsum</p>

    <p class="website">Visit us : www.website.com</p>
  </main>
</body>
</html>
```